New minimal and cool business card

We have a brand new logo - we would like to use the logo on blue on the front of the card
The tagline is The give and take network (tm)
We would like information on the back of the card for individual(s)

Our font is Lato
Our colors are indicated in the attached identity guide which uses the old logo - we are de-emphasizing orange

Please prepare the artwork to meet the specs on this site
http://us.pirvex.com/products/sheen/business-cards.html

Front: Logo and tagline on dark blue

Back: On white
Join Today
http://ourtandem.co/join

```html
<!DOCTYPE html>
<html lang="en">
<head>
<meta charset="utf-8">
<title>ourtandem business card</title>
<link rel="stylesheet" href="https://fonts.googleapis.com/css2?family=Lato:wght@300;400;700&display=swap">
<style>
  :root {
    --canvas: #e6e9ed;
    --card-navy: #34495f;
    --card-white: #ffffff;
    --ink-light: #ffffff;
    --ink-soft: #dfe4ea;
    --logo-grey: #c9ced4;
    --icon-fill: #ffffff;
    --icon-ink: #34495f;
  }
  * { box-sizing: border-box; margin: 0; padding: 0; }
  html, body {
    width: 1200px;
    height: 672px;
    overflow: hidden;
    background: var(--canvas);
    font-family: "Lato", sans-serif;
  }
  .stage {
    width: 1200px;
    height: 672px;
    display: flex;
    align-items: center;
    justify-content: center;
    gap: 64px;
  }
  .business-card {
    position: relative;
    width: 330px;
    height: 576px;
    box-shadow: 0 6px 22px rgba(30, 40, 55, 0.22);
  }
  .card-front {
    background: var(--card-navy);
    color: var(--ink-light);
  }
  .card-back {
    background: var(--card-white);
    color: var(--card-navy);
    display: flex;
    flex-direction: column;
    align-items: center;
    justify-content: center;
    text-align: center;
    gap: 14px;
  }
  .brand {
    position: absolute;
    top: 112px;
    right: 36px;
    text-align: right;
  }
  .brand-row {
    display: flex;
    align-items: center;
    justify-content: flex-end;
    gap: 9px;
  }
  .brand-name {
    font-weight: 300;
    font-size: 42px;
    letter-spacing: 1px;
    line-height: 1;
    color: var(--logo-grey);
  }
  .brand-dot {
    width: 9px;
    height: 9px;
    border-radius: 50%;
    background: var(--logo-grey);
  }
  .tagline {
    margin-top: 10px;
    padding-right: 18px;
    font-size: 10px;
    letter-spacing: 2px;
    text-transform: uppercase;
    color: var(--ink-soft);
  }
  .person {
    position: absolute;
    top: 304px;
    left: 32px;
  }
  .person-name {
    font-weight: 400;
    font-size: 24px;
    letter-spacing: 1.5px;
    text-transform: uppercase;
  }
  .person-role {
    margin-top: 3px;
    font-size: 10px;
    letter-spacing: 1.4px;
    text-transform: uppercase;
    color: var(--ink-soft);
  }
  .contact-list {
    position: absolute;
    top: 368px;
    left: 32px;
    right: 24px;
    list-style: none;
  }
  .contact-item {
    display: flex;
    align-items: flex-start;
    gap: 12px;
    margin-bottom: 11px;
    font-size: 12px;
    line-height: 17px;
    letter-spacing: 0.6px;
    color: var(--ink-soft);
  }
  .contact-icon {
    flex: none;
    width: 17px;
    height: 17px;
    border-radius: 3px;
    background: var(--icon-fill);
    display: flex;
    align-items: center;
    justify-content: center;
  }
  .contact-icon svg { width: 11px; height: 11px; fill: var(--icon-ink); }
  .join-title {
    font-weight: 700;
    font-size: 30px;
    letter-spacing: 2px;
    text-transform: uppercase;
  }
  .join-link {
    font-size: 13px;
    letter-spacing: 0.6px;
  }
</style>
</head>
<body>
<main class="stage">
  <article class="business-card card-back">
    <h2 class="join-title">Join Today</h2>
    <p class="join-link">http://ourtandem.co/join</p>
  </article>

  <article class="business-card card-front">
    <div class="brand">
      <div class="brand-row">
        <span class="brand-name">ourtandem</span>
        <span class="brand-dot"></span>
      </div>
      <p class="tagline">The give and take network&trade;</p>
    </div>

    <div class="person">
      <h1 class="person-name">Alex Carter</h1>
      <p class="person-role">General Manager</p>
    </div>

    <ul class="contact-list">
      <li class="contact-item">
        <span class="contact-icon"><svg viewBox="0 0 12 12"><path d="M2.5 1h2l1 3-1.3 1a6 6 0 0 0 2.8 2.8L8 6.5l3 1v2a1.5 1.5 0 0 1-1.5 1.5A8.5 8.5 0 0 1 1 2.5 1.5 1.5 0 0 1 2.5 1z"/></svg></span>
        <span>014 572 3380</span>
      </li>
      <li class="contact-item">
        <span class="contact-icon"><svg viewBox="0 0 12 12"><path d="M3.5 0.5h5a1 1 0 0 1 1 1v9a1 1 0 0 1-1 1h-5a1 1 0 0 1-1-1v-9a1 1 0 0 1 1-1zm0.5 1.5v7h4V2zm2 7.6a0.6 0.6 0 1 0 0 1.2 0.6 0.6 0 0 0 0-1.2z"/></svg></span>
        <span>014 572 3391</span>
      </li>
      <li class="contact-item">
        <span class="contact-icon"><svg viewBox="0 0 12 12"><path d="M1 2.5h10v7H1zm1 1v0.4l4 2.6 4-2.6V3.5zm0 1.6v3.4h8V5.1L6 7.7z"/></svg></span>
        <span>alex.carter@ourtandem.co</span>
      </li>
      <li class="contact-item">
        <span class="contact-icon"><svg viewBox="0 0 12 12"><path d="M6 0.8a5.2 5.2 0 1 0 0 10.4A5.2 5.2 0 0 0 6 0.8zm0 1.1c0.7 0.6 1.2 1.9 1.3 3.5H4.7C4.8 3.8 5.3 2.5 6 1.9zM3.6 5.4H1.9a4.1 4.1 0 0 1 2.5-3.2 6.6 6.6 0 0 0-0.8 3.2zm0 1.2a6.6 6.6 0 0 0 0.8 3.2 4.1 4.1 0 0 1-2.5-3.2zm1.1 0h2.6C7.2 8.2 6.7 9.5 6 10.1 5.3 9.5 4.8 8.2 4.7 6.6zm3.7 0h1.7a4.1 4.1 0 0 1-2.5 3.2 6.6 6.6 0 0 0 0.8-3.2zm0-1.2a6.6 6.6 0 0 0-0.8-3.2 4.1 4.1 0 0 1 2.5 3.2z"/></svg></span>
        <span>www.ourtandem.co</span>
      </li>
      <li class="contact-item">
        <span class="contact-icon"><svg viewBox="0 0 12 12"><path d="M6 0.6a4 4 0 0 0-4 4c0 3 4 6.8 4 6.8s4-3.8 4-6.8a4 4 0 0 0-4-4zm0 2.4a1.6 1.6 0 1 1 0 3.2 1.6 1.6 0 0 1 0-3.2z"/></svg></span>
        <span>27, 9th Floor, Harbor View<br>Road, NTX</span>
      </li>
    </ul>
  </article>
</main>
</body>
</html>
```